Property Service business needs a cool business card

Looking for an eloquent and unique business card using the logo and colours attached as uploaded files.

Target Market(s)

Body corporates, real estate agents, building managers

Industry/Entity Type

Business

Contact Information for Business Card

- Kelvo Logo
- Construction * Maintenance * Remedial

- Ned Pirrick
- Business Manager

- Ph 0417586043
- P.O Box 514 South Melbourne Vic 3090
- Email ned@kelvo.com
- Website www.kelvopropertyservices.com.au

Requirements
Must have
• Clean and fresh look, colours must be vibrant!
Nice to have
• unique features
Should not have
• Should not be overcrowded

```html
<!DOCTYPE html>
<html lang="en">
<head>
<meta charset="utf-8">
<title>Kelvo Business Card</title>
<link href="https://fonts.googleapis.com/css2?family=Open+Sans:wght@400;600;700&display=swap" rel="stylesheet">
<style>
  :root {
    --backdrop: #e9e9e9;
    --card-white: #fbfbfb;
    --brand-blue: #0d5aa7;
    --brand-green: #8cc63f;
    --ink: #3a3a3a;
    --muted: #6a6a6a;
    --white: #ffffff;
  }
  * { margin: 0; padding: 0; box-sizing: border-box; }
  html, body {
    width: 1200px;
    height: 900px;
    overflow: hidden;
    background: var(--backdrop);
    font-family: "Open Sans", Arial, sans-serif;
  }
  .canvas {
    position: relative;
    width: 1200px;
    height: 900px;
    display: flex;
    align-items: center;
    justify-content: center;
    gap: 60px;
  }
  .card {
    position: relative;
    width: 500px;
    height: 286px;
    box-shadow: 0 2px 6px rgba(0,0,0,0.12);
  }
  .card-front { background: var(--card-white); }
  .card-back {
    background: var(--brand-blue);
    display: flex;
    align-items: center;
    justify-content: center;
  }
  .holder {
    position: absolute;
    left: 34px;
    top: 32px;
  }
  .holder-name {
    color: var(--brand-blue);
    font-weight: 700;
    font-size: 21px;
    line-height: 1.1;
  }
  .holder-role {
    color: var(--muted);
    font-size: 12px;
    margin-top: 3px;
  }
  .contact {
    position: absolute;
    left: 34px;
    top: 118px;
    list-style: none;
    font-size: 13px;
    line-height: 1.15;
  }
  .contact-label { color: var(--brand-blue); display: block; }
  .contact-value { color: var(--ink); display: block; margin-bottom: 2px; }
  .wordmark {
    display: flex;
    align-items: center;
    gap: 10px;
    font-weight: 600;
    letter-spacing: 1px;
  }
  .card-front .wordmark {
    position: absolute;
    right: 40px;
    top: 150px;
    color: var(--brand-blue);
    font-size: 44px;
  }
  .card-back .wordmark {
    color: var(--white);
    font-size: 44px;
  }
  .wordmark-square {
    width: 34px;
    height: 34px;
    background: var(--brand-green);
  }
</style>
</head>
<body>
  <main class="canvas">
    <section class="card card-front">
      <div class="holder">
        <p class="holder-name">Colm Varden</p>
        <p class="holder-role">Managing Director</p>
      </div>
      <ul class="contact">
        <li><span class="contact-label">telephone</span><span class="contact-value">044-527 318 906</span></li>
        <li><span class="contact-label">email</span><span class="contact-value">info@kelvoweb.com</span></li>
        <li><span class="contact-label">address</span><span class="contact-value">4817, address goes here, country</span></li>
      </ul>
      <div class="wordmark">
        <span class="wordmark-square"></span>
        <span class="wordmark-name">Kelvo</span>
      </div>
    </section>
    <section class="card card-back">
      <div class="wordmark">
        <span class="wordmark-square"></span>
        <span class="wordmark-name">Kelvo</span>
      </div>
    </section>
  </main>
</body>
</html>
```